Business Card for Pottery and Jewellery Designer

A new business card design is needed to accompany a newly launching pottery and jewellery website. The company logo has been attached for use. The company is called Glazewick Studio. For a sense of the vibe please see the website (it is currently under construction but this way you'll get a feel for the style) www.GlazewickStudio.com

The website font is Pontano Sans for the body of the text with Overlock for headers.

The overall look should be clean and elegant. The back side can have just the logo. The front side should have a smaller logo and the following details displayed:

Glazewick Studio
Designer: Hollis Marrow
Phone: xxx.xxx.xxxx
Email: Designer@GlazewickStudio.com

The structure of displaying this is completely up to you. Different layouts and creative methods of displaying contact info are welcome as long as it stays clean/uncluttered.

No product photographs are to be included in the design as the catalogue changes quickly.

Colour preferences lean towards elegant and understated (charcoal grey, dark navy blue etc.)

Please let me know if you have any further questions or further details required.

Target Market(s)

Target market is 30+ year old women

Industry/Entity Type

Construction

Colors
ffffff
1b1b1b
474747
d9d9d9
fafafa
0355a3

Requirements
Must have
• The submissions so far have looked very typical and don't stand out right now. They're also all in navy with very little variation. I'm looking for something that stands out a it more while still being clean-looking.
Nice to have
• I've attached a few design samples and an idea for a backdrop. It would be great to see some designs in black, white, and grey with only a hint of color.
Should not have
• Product Images

```html
<!DOCTYPE html>
<html lang="en">
<head>
<meta charset="utf-8">
<title>Glazewick Studio — Business Card</title>
<link rel="stylesheet" href="https://fonts.googleapis.com/css2?family=Pontano+Sans:wght@300;400;700&display=swap">
<style>
  :root {
    --paper: #ffffff;
    --ink: #1b1b1b;
    --charcoal: #474747;
    --mist: #d9d9d9;
    --backdrop: #ece9e4;
    --hint: #0355a3;
  }
  * { box-sizing: border-box; margin: 0; padding: 0; }
  html, body {
    width: 1200px;
    height: 1023px;
    overflow: hidden;
    background: var(--backdrop);
    font-family: "Pontano Sans", "Helvetica Neue", Arial, sans-serif;
    color: var(--ink);
  }
  .sheet {
    position: relative;
    width: 1200px;
    height: 1023px;
  }
  .card {
    position: absolute;
    width: 640px;
    height: 366px;
    background: var(--paper);
    border: 16px solid var(--charcoal);
    box-shadow: 0 10px 24px rgba(0,0,0,0.18);
  }
  .card--back { left: 120px; top: 90px; }
  .card--front { left: 440px; top: 560px; }

  /* back: brand mark area */
  .brand-large {
    position: absolute;
    inset: 0;
    display: flex;
    align-items: center;
    justify-content: center;
    gap: 18px;
  }
  .brand-large__dot {
    width: 56px;
    height: 56px;
    border-radius: 50%;
    background: var(--charcoal);
  }
  .brand-large__name {
    font-size: 40px;
    font-weight: 400;
    letter-spacing: 1px;
    color: var(--charcoal);
    text-transform: uppercase;
  }

  /* front */
  .brand-small {
    position: absolute;
    left: 26px;
    top: 22px;
  }
  .brand-small__dot {
    display: block;
    width: 22px;
    height: 22px;
    border-radius: 50%;
    background: var(--charcoal);
    margin-bottom: 6px;
  }
  .brand-small__name {
    font-size: 19px;
    font-weight: 400;
    letter-spacing: 0.5px;
    text-transform: uppercase;
    color: var(--ink);
  }
  .person {
    position: absolute;
    right: 30px;
    top: 200px;
    text-align: right;
  }
  .person__name {
    font-size: 22px;
    font-weight: 700;
    color: var(--ink);
  }
  .person__role {
    font-size: 15px;
    color: var(--charcoal);
    margin-top: 2px;
  }
  .contact {
    position: absolute;
    left: 26px;
    bottom: 22px;
    display: flex;
    gap: 60px;
    font-size: 15px;
    color: var(--ink);
  }
  .contact__item {
    display: flex;
    align-items: center;
    gap: 8px;
  }
  .contact__icon {
    width: 18px;
    height: 18px;
    flex: none;
  }
</style>
</head>
<body>
<main class="sheet">
  <section class="card card--back" aria-label="Card back">
    <div class="brand-large">
      <span class="brand-large__dot"></span>
      <span class="brand-large__name">Glazewick Studio</span>
    </div>
  </section>

  <section class="card card--front" aria-label="Card front">
    <div class="brand-small">
      <span class="brand-small__dot"></span>
      <span class="brand-small__name">Glazewick Studio</span>
    </div>

    <div class="person">
      <p class="person__name">Hollis Marrow</p>
      <p class="person__role">Designer</p>
    </div>

    <div class="contact">
      <p class="contact__item">
        <svg class="contact__icon" viewBox="0 0 18 18" aria-hidden="true">
          <circle cx="9" cy="9" r="9" fill="#474747"/>
          <path d="M5.5 5.2c.6-.6 1.3-.5 1.6 0l.8 1.3c.3.5.2 1-.2 1.3l-.5.4c.4 1 1.2 1.8 2.2 2.3l.4-.5c.4-.4.9-.5 1.3-.2l1.3.8c.5.3.6 1 0 1.6-.8.8-2 1-3.3.3-1.6-.9-3-2.3-3.9-3.9-.7-1.3-.5-2.6.3-3.4z" fill="#ffffff"/>
        </svg>
        <span>xxx.xxx.xxxx</span>
      </p>
      <p class="contact__item">
        <svg class="contact__icon" viewBox="0 0 18 18" aria-hidden="true">
          <circle cx="9" cy="9" r="9" fill="#474747"/>
          <rect x="4.5" y="6" width="9" height="6.5" rx="0.8" fill="none" stroke="#ffffff" stroke-width="1.2"/>
          <path d="M4.8 6.4 9 9.6l4.2-3.2" fill="none" stroke="#ffffff" stroke-width="1.2"/>
        </svg>
        <span>Designer@GlazewickStudio.com</span>
      </p>
    </div>
  </section>
</main>
</body>
</html>
```